Hispanic Financial Counseling and Advocate Firm seeks business card design

Looking for a clean, professional business card design. This is a firm that specializes in providing financial education, coaching, and planning to the Hispanic community. The name of the company is Valemar, which means to prosper. We need a design that is clean, professional, and invokes trust, professionalism, but also welcoming. Our logo is a plant growing from a hand to give the messaging of of being in control of growing your financial future and security. Its part of a larger organization names Celesta Financial Group, who's logo is a tree with multi colored branches. We have the back of the card designed so we just need the front designed. the back is blue, so front needs to be a different background color, not blue.

Target Market(s)

Hispanic Community looking to better their future

Industry/Entity Type

financial services

Contact Information for Business Card

contact info: Anselmo Ibarra Jr, 951-555-0147, info@celestafinancialgroup.example. Celestafinancialgroup.example. tag line: Para un futuro mas seguro!

Requirements
Must have
• basics: logo, contact info.
Nice to have
• possibly incorporate the tree logo provided somehow
Should not have
• should not look like the back, needs to be different from the back provided.

```html
<!DOCTYPE html>
<html lang="es">
<head>
<meta charset="utf-8">
<title>Valemar – Tarjeta de presentación</title>
<link rel="stylesheet" href="https://fonts.googleapis.com/css2?family=Open+Sans:wght@400;600;700&display=swap">
<style>
  :root {
    --stage: #2b2b2d;
    --card: #ffffff;
    --card-shade: #eeeeee;
    --green: #5aa53a;
    --navy: #475872;
    --ink: #4a4a4a;
    --band-text: #ffffff;
  }
  * { margin: 0; padding: 0; box-sizing: border-box; }
  html, body {
    width: 1200px; height: 900px; overflow: hidden;
    background: var(--stage);
    font-family: "Open Sans", sans-serif;
  }
  .canvas {
    width: 1200px; height: 900px;
    display: flex; align-items: center; justify-content: center;
  }
  .business-card {
    position: relative;
    width: 1000px; height: 571px;
    background: linear-gradient(100deg, var(--card) 0%, var(--card) 55%, var(--card-shade) 100%);
    overflow: hidden;
    box-shadow: 0 20px 50px rgba(0,0,0,0.45);
  }
  .footer-band { position: absolute; left: 0; top: 0; width: 1000px; height: 571px; }
  .brand {
    position: absolute; left: 64px; top: 138px;
    display: flex; align-items: center; gap: 18px;
  }
  .brand-dot {
    width: 34px; height: 34px; border-radius: 50%;
    background: var(--green); flex: none;
  }
  .brand-name {
    font-size: 70px; font-weight: 600; color: var(--green);
    letter-spacing: -1px; line-height: 1;
  }
  .holder-name {
    position: absolute; right: 86px; top: 92px;
    font-size: 27px; font-weight: 700; color: var(--green);
    text-transform: uppercase; letter-spacing: 0.5px;
  }
  .contact-list {
    position: absolute; left: 96px; top: 262px;
    list-style: none;
  }
  .contact-item {
    display: flex; align-items: center; gap: 14px;
    height: 44px;
    font-size: 26px; color: var(--ink);
  }
  .contact-icon { width: 22px; height: 22px; flex: none; }
  .tagline {
    position: absolute; left: 78px; bottom: 24px;
    font-size: 36px; font-weight: 400; color: var(--band-text);
  }
</style>
</head>
<body>
<main class="canvas">
  <article class="business-card">
    <svg class="footer-band" viewBox="0 0 1000 571" aria-hidden="true">
      <polygon points="0,488 1000,420 1000,571 0,571" fill="var(--navy)"/>
    </svg>

    <div class="brand">
      <span class="brand-dot" aria-hidden="true"></span>
      <h1 class="brand-name">Valemar</h1>
    </div>
    <p class="holder-name">Anselmo Ibarra Jr</p>

    <ul class="contact-list">
      <li class="contact-item">
        <svg class="contact-icon" viewBox="0 0 24 24" aria-hidden="true">
          <path fill="var(--navy)" d="M3 9c0-3 4-5 9-5s9 2 9 5v2h-5V8.5c-2-.6-6-.6-8 0V11H3zM6 12h12l2 8H4z"/>
          <circle cx="12" cy="16" r="2.2" fill="#fff"/>
        </svg>
        <span>951-555-0147</span>
      </li>
      <li class="contact-item">
        <svg class="contact-icon" viewBox="0 0 24 24" aria-hidden="true">
          <circle cx="12" cy="12" r="10" fill="var(--navy)"/>
          <path d="M2 12h20M12 2c3 3 3 17 0 20M12 2c-3 3-3 17 0 20" stroke="#fff" stroke-width="1.4" fill="none"/>
        </svg>
        <span>Celestafinancialgroup.example</span>
      </li>
      <li class="contact-item">
        <svg class="contact-icon" viewBox="0 0 24 24" aria-hidden="true">
          <rect x="2" y="5" width="20" height="14" rx="1.5" fill="var(--navy)"/>
          <path d="M3 6l9 7 9-7" stroke="#fff" stroke-width="1.6" fill="none"/>
        </svg>
        <span>info@celestafinancialgroup.example</span>
      </li>
    </ul>

    <p class="tagline">Para un futuro mas seguro!</p>
  </article>
</main>
</body>
</html>
```